Souvenir and Health Food Products

We need a website designed for a Wholesaler & Distributor of Australia Made Souvenir & Health Food products. Our range includes many of Australia's leading brands: Willow's Cottage, Southern Meadow Essentials, Pebble & Ferne, Vanto Cosmetics, Drelona, K T Leathergoods, Trestin Leathergoods, Brekker's Salt & Tallowick Honey.

Design will be converted into a Dot Net Nuke skin and containers so needs to be compatible.

Needs to show off their products and be easy to navigate.

Would like a nice clean and corporate look.
Updates

Hi Everyone

All design concepts are with my client who has been extremely busy....hoping to get feedback from them this week.

Cheers
Mabel

Target Market(s)

Target market are retail shops looking to stock their products

Industry/Entity Type

Health

Number of Pages Required

2 pages

Requirements
Must have
• Proposed Site Map
• Home
• About Us
• Products
• Ordering
• Contact Us

• To be included in homepage design concept:

• Large area for a flash banner of rotating images on homepage
• Logo and Phone number in header for every page 07 5000 3172
• Some welcome text
• Some icons will need to be designed - Register for our newsletter and Contact Us
• Product category list on homepage – thumbnail image/name of category (click through)

• Product categories to use are:
• (allow for up to 15)
• • Willow’s Cottage (use p1000321/jpg)

• • Jojoba Oil (use TFP_0121.jpg))

• • Southern Meadow Essentials (use TFP_0077.jpg)

• Could you create a separate content page to show how products will look on category page with each product having a thumbnail image, description and Enquire now button.
Should not have
• No shopping cart or ecommerce needed

```html
<!DOCTYPE html>
<html lang="en">
<head>
<meta charset="utf-8">
<title>Kestrel Trading – Website Concepts</title>
<link rel="stylesheet" href="https://fonts.googleapis.com/css2?family=Open+Sans:wght@300;400;600;700&family=Tinos&display=swap">
<style>
  :root{
    --board:#7aa93a;
    --paper:#ffffff;
    --green:#8dbb2e;
    --green-dark:#6e9a2a;
    --banner-light:#c3da73;
    --banner-dark:#7ea83b;
    --blue:#3eaee5;
    --blue-dark:#2a93cc;
    --orange:#ef5a1f;
    --red-link:#d9361e;
    --ink:#222;
    --muted:#666;
    --rule:#dcdcdc;
    --footer:#efefed;
  }
  *{box-sizing:border-box;margin:0;padding:0}
  html,body{width:1200px;height:483px;overflow:hidden;background:var(--board);font-family:"Open Sans",Arial,sans-serif;color:var(--ink)}
  .board{position:relative;width:1200px;height:483px}
  .page{position:absolute;top:16px;width:362px;height:422px;background:var(--paper);box-shadow:2px 3px 4px rgba(0,0,0,.35);overflow:hidden}
  .page--home-a{left:43px}
  .page--home-b{left:424px}
  .page--product{left:797px}
  .caption{position:absolute;top:444px;width:362px;text-align:center;font-family:"Tinos",serif;font-size:16px;letter-spacing:.5px;color:#1a1a1a}
  .abs{position:absolute}

  /* header */
  .brand{left:16px;top:12px;display:flex;align-items:center;gap:4px}
  .brand__dot{width:14px;height:14px;border-radius:50%;background:var(--blue)}
  .brand__name{font-size:9px;font-weight:700;color:#111;letter-spacing:.6px;text-transform:uppercase}
  .phone{right:15px;top:4px;display:flex;align-items:center;gap:3px;color:var(--green);font-weight:300;font-size:15px;letter-spacing:-.2px}
  .nav{right:10px;top:24px;display:flex;gap:9px;font-size:4.8px;color:#333}
  .nav span::after{content:" →";color:var(--orange);font-size:4px}

  /* banner */
  .banner{left:11px;top:42px;width:341px;height:110px;background:radial-gradient(ellipse at 60% 45%,var(--banner-light),var(--banner-dark) 80%);border-bottom:1px solid #b5cf6d}
  .banner__photo{position:absolute;left:22px;top:2px;width:120px;height:108px;background:linear-gradient(160deg,#b3283a,#d8a23a 70%,#e4c55a);opacity:.85;border-radius:2px}
  .banner__photo--green{background:linear-gradient(160deg,#d7d2b8,#6b8f3b 60%,#c9c7a8)}
  .banner__title{position:absolute;left:172px;top:15px;font-size:15.5px;font-weight:300;color:#fff;letter-spacing:-.2px}
  .banner__text{position:absolute;left:173px;top:44px;width:160px;font-size:8.3px;font-weight:300;line-height:9px;color:#f4f8e6}
  .banner__button{position:absolute;left:205px;top:78px;width:117px;height:14px;background:linear-gradient(var(--blue),var(--blue-dark));color:#fff;font-size:5.6px;text-align:center;line-height:14px}

  /* featured */
  .featured{left:11px;top:171px;width:87px;height:178px;border:1px solid #e0e0e0;background:#f4f4f4}
  .featured__head{height:13px;background:var(--blue);color:#fff;font-size:6px;line-height:13px;padding-left:9px}
  .card{margin:3px 3px 0;background:#fff;height:78px;padding:2px 4px;position:relative}
  .card__photo{height:38px;background:linear-gradient(#f7f7f2,#c9d3a8);border-radius:2px}
  .card__photo--mix{background:linear-gradient(120deg,#e7eef4,#b8cfe0 40%,#e4a6a1 70%,#eef0f0)}
  .card__name{font-size:3.8px;font-weight:700;color:var(--red-link);text-decoration:underline;margin-top:3px;letter-spacing:.3px}
  .card__text{font-size:3.6px;line-height:4.6px;color:#444}
  .card__buy{position:absolute;left:7px;bottom:3px;font-size:3.8px;font-weight:700;text-decoration:underline}
  .card__buy::before{content:"● ";color:var(--orange)}
  .card__price{position:absolute;right:6px;bottom:2px;font-size:7px}

  /* middle column */
  .block{left:116px;width:134px}
  .block__title{font-size:8px;line-height:8px;letter-spacing:-.1px}
  .block__title .go{display:inline-block;width:6px;height:6px;border-radius:50%;background:var(--orange);vertical-align:middle;margin-left:2px}
  .block__lead{font-size:3.8px;font-style:italic;font-weight:700;margin-top:5px}
  .block__text{font-size:3.8px;line-height:5px;color:#555}
  .block__rule{left:116px;width:134px;height:1px;background:var(--rule)}
  .icon{width:28px;height:34px}
  .block__body{left:141px;width:109px}

  /* news */
  .news{left:269px;top:171px;width:83px;height:118px;border:1px solid #dedede}
  .news__head{height:14px;background:linear-gradient(#fff,#ececec);font-size:6px;line-height:14px;padding-left:6px;font-weight:600;color:#333}
  .news__item{padding:6px 6px 0}
  .news__title{font-size:3.8px;font-weight:700;letter-spacing:.2px}
  .news__date{font-size:3.6px;color:#999;margin:1px 0 2px}
  .news__text{font-size:3.6px;line-height:4.8px;color:#555}
  .news__text u{color:var(--red-link)}

  /* badge */
  .badge{left:284px;top:300px;width:60px;height:60px}
  .badge__text{position:absolute;left:284px;top:312px;width:58px;text-align:center;color:#fff}
  .badge__big{font-size:15px;font-weight:300;line-height:15px}
  .badge__small{font-size:6px;font-weight:600}
  .badge__link{font-size:6.5px;color:#e8f39a;text-decoration:underline;margin-top:2px}

  /* footer */
  .footer{left:11px;top:383px;width:341px;height:39px;background:var(--footer);border-top:1px solid var(--green)}
  .footer__links{position:absolute;left:11px;top:9px;font-size:4.5px;color:#555;word-spacing:1px}

  /* product page */
  .dropdown{left:257px;top:36px;width:53px;font-size:4px;text-transform:uppercase;color:#555}
  .dropdown__top{height:8px;line-height:8px;padding-left:1px;background:#fff}
  .dropdown__item{height:7.7px;line-height:7.7px;padding-left:2px;background:#f4f8e4;border-bottom:.5px solid #c7d99a}
  .dropdown__item--on{background:#dfeab6}
  .product__title{left:21px;top:175px;font-size:9px}
  .product__list{left:21px;top:192px;width:130px}
  .product__lead{font-size:3.9px;font-style:italic;font-weight:700;margin-top:5px}
  .product__text{font-size:3.9px;color:#555}
  .enquire{left:21px;top:298px;width:62px;height:8px;background:var(--blue);color:#fff;font-size:5px;text-align:center;line-height:8px}
  .product__photo{left:182px;top:171px;width:168px;height:125px;background:radial-gradient(ellipse at 50% 55%,#5f8a4c,#b9c9a3 45%,#f0f0ee 75%)}
  .strip__rule{left:11px;top:347px;width:341px;height:1px;background:#b8d06b}
  .strip{left:11px;top:352px;width:341px;height:27px;display:flex;align-items:center;gap:4px}
  .strip__thumb{width:36px;height:25px;background:linear-gradient(#eef2f4,#a9c9b6)}
  .strip__thumb--soap{background:linear-gradient(#eeeeea,#a4a878)}
  .strip__thumb--red{background:linear-gradient(#f0e8e0,#b3283a 60%,#d9a33a)}
</style>
</head>
<body>
<div class="board">

  <!-- Home page concept A -->
  <section class="page page--home-a">
    <div class="abs brand"><span class="brand__dot"></span><span class="brand__name">Kestrel Trading</span></div>
    <div class="abs phone">
      <svg width="11" height="11" viewBox="0 0 12 12"><rect width="12" height="12" rx="2" fill="#8dbb2e"/><path d="M3.5 2.5c.6-.3 1.2 0 1.4.6l.4 1.2c.1.4-.1.8-.4 1l-.4.3c.4.9 1.1 1.6 2 2l.3-.4c.3-.3.7-.5 1-.4l1.2.4c.6.2.9.8.6 1.4-.4.8-1.3 1.2-2.2.9C5.3 8.8 3.2 6.7 2.6 4.6c-.3-.9.1-1.8.9-2.1z" fill="#fff"/></svg>
      07 5000 3172
    </div>
    <nav class="abs nav"><span>Home</span><span>About Us</span><span>Products</span><span>Ordering</span><span>Contact Us</span></nav>

    <div class="abs banner">
      <div class="banner__photo" role="img" aria-label="Photo of jojoba oil bottles and red gift boxes"></div>
      <div class="banner__title">Welcome to Our Site!</div>
      <p class="banner__text">Sed ut perspiciatis unde omnis iste natus error sit voluptatem accustium doremque launtium.</p>
      <div class="banner__button">CLICK HERE TO LEARN MORE</div>
    </div>

    <aside class="abs featured">
      <div class="featured__head">Featured Products</div>
      <div class="card">
        <div class="card__photo" role="img" aria-label="Photo of health supplement jars"></div>
        <div class="card__name">LOREM IPSUM DOLOR SIT</div>
        <p class="card__text">Consectetur adipiscing elit, sed iusmod tempor incididunt utabore olore magna aliqua.</p>
        <span class="card__buy">buy now</span><span class="card__price">$00.00</span>
      </div>
      <div class="card">
        <div class="card__photo card__photo--mix" role="img" aria-label="Photo of assorted skincare products"></div>
        <div class="card__name">IPSUM DOLOR SIT</div>
        <p class="card__text">Consectetur adipiscing elit, sed iusmod tempor incid utaboreolore magna aliqua.</p>
        <span class="card__buy">buy now</span><span class="card__price">$00.00</span>
      </div>
    </aside>

    <div class="abs block" style="top:174px">
      <h2 class="block__title" style="font-weight:400">Sed ut perspiciatis unde omnis natus error sitvolup<span class="go"></span></h2>
      <p class="block__lead">Sed ut perspiciatis unde omnis iste natus</p>
      <p class="block__text">Error itatem accusantium doloremque laudanti ttam aperiam, eue ipsa quae ab illo inventore veritteasi archecto beatatae dicta sunt explicabo. Nemoipsam oluptatem quia voluptas.</p>
    </div>
    <div class="abs block__rule" style="top:232px"></div>
    <div class="abs block" style="top:249px"><h2 class="block__title" style="font-weight:400">Register for our newsletter<span class="go"></span></h2></div>
    <svg class="abs icon" style="left:119px;top:265px" viewBox="0 0 28 34"><rect x="4" y="3" width="16" height="22" rx="1" fill="#3fa33a" transform="rotate(-12 12 14)"/><rect x="6" y="5" width="12" height="18" fill="#e8f2d8" transform="rotate(-12 12 14)"/><line x1="12" y1="28" x2="25" y2="10" stroke="#333" stroke-width="2"/></svg>
    <div class="abs block__body" style="top:264px">
      <p class="block__lead" style="margin:0">Perspiciatis unde omnis iste natus</p>
      <p class="block__text">Error itatem accusantium doloremque laudanti totam aperiam, eue ipsa quae ab illo inventore veritis easi archecto beatatae dicta sunt explicabo. Nemo ipsam oluptatem quia voluptas sit aspernatur.</p>
    </div>
    <div class="abs block__rule" style="top:302px"></div>
    <div class="abs block" style="top:318px"><h2 class="block__title" style="font-weight:400">Contact Us<span class="go"></span></h2></div>
    <svg class="abs icon" style="left:119px;top:333px" viewBox="0 0 28 34"><rect x="3" y="8" width="22" height="18" rx="3" fill="#4a8a4a"/><rect x="7" y="4" width="14" height="6" rx="3" fill="#2e6b35"/><rect x="8" y="12" width="12" height="10" fill="#dfe9d6"/></svg>
    <div class="abs block__body" style="top:334px">
      <p class="block__lead" style="margin:0">Error itatem accusantium</p>
      <p class="block__text">Dolremque laudantium, totam aperiam, e ipsa quae ab illo inventore veritatis easi archecto beatatae dicta sunt explicabo. Nemo ipsam oluptatem quia voluptas sit aspernatur.</p>
    </div>

    <div class="abs news">
      <div class="news__head">News &amp; Events</div>
      <div class="news__item">
        <div class="news__title">Unde omnis iste natus error itatem</div>
        <div class="news__date">Posted: 12/07/2008</div>
        <p class="news__text">Doloremque laudantium, tperiam, eue ipsa quae <u>ab illontore veritatis</u> easi archecto beatatae.</p>
      </div>
      <div class="news__item" style="padding-top:9px">
        <div class="news__title">Doloremque laudantiu tperiam</div>
        <div class="news__date">Posted: 12/07/2008</div>
        <p class="news__text">Daudantium, tperiam, eue ipsquae ab illontore veritatis easi archecto beatatadicta <u>sunt explicabo</u>. Nemo ipsam oluptatem quiae</p>
      </div>
    </div>

    <svg class="abs badge" viewBox="0 0 60 60"><defs><radialGradient id="bgA" cx=".4" cy=".35"><stop offset="0" stop-color="#a8cf45"/><stop offset="1" stop-color="#5e9425"/></radialGradient></defs><circle cx="30" cy="30" r="29" fill="url(#bgA)"/><path d="M44 4 L58 18 L46 16 Z" fill="#e9efe0"/></svg>
    <div class="badge__text">
      <div class="badge__big">-5%</div>
      <div class="badge__small">by online order</div>
      <div class="badge__link">click here</div>
    </div>

    <footer class="abs footer"><div class="footer__links">Company &nbsp;|&nbsp; Products &nbsp;|&nbsp; Download &nbsp;|&nbsp; Support &nbsp;|&nbsp; Contacts</div></footer>
  </section>
  <div class="caption" style="left:43px">HOME PAGE</div>

  <!-- Home page concept B -->
  <section class="page page--home-b">
    <div class="abs brand"><span class="brand__dot"></span><span class="brand__name">Kestrel Trading</span></div>
    <div class="abs phone">
      <svg width="11" height="11" viewBox="0 0 12 12"><rect width="12" height="12" rx="2" fill="#8dbb2e"/><path d="M3.5 2.5c.6-.3 1.2 0 1.4.6l.4 1.2c.1.4-.1.8-.4 1l-.4.3c.4.9 1.1 1.6 2 2l.3-.4c.3-.3.7-.5 1-.4l1.2.4c.6.2.9.8.6 1.4-.4.8-1.3 1.2-2.2.9C5.3 8.8 3.2 6.7 2.6 4.6c-.3-.9.1-1.8.9-2.1z" fill="#fff"/></svg>
      07 5000 3172
    </div>
    <nav class="abs nav"><span>Home</span><span>About Us</span><span>Products</span><span>Ordering</span><span>Contact Us</span></nav>

    <div class="abs banner">
      <div class="banner__photo banner__photo--green" role="img" aria-label="Photo of eucalyptus cream, soap and oil products"></div>
      <div class="banner__title">Welcome to Our Site!</div>
      <p class="banner__text">Sed ut perspiciatis unde omnis iste natus error sit voluptatem accustium doremque launtium.</p>
      <div class="banner__button">CLICK HERE TO LEARN MORE</div>
    </div>

    <aside class="abs featured">
      <div class="featured__head">Featured Products</div>
      <div class="card">
        <div class="card__photo" role="img" aria-label="Photo of health supplement jars"></div>
        <div class="card__name">LOREM IPSUM DOLOR SIT</div>
        <p class="card__text">Consectetur adipiscing elit, sed iusmod tempor incididunt utabore olore magna aliqua.</p>
        <span class="card__buy">buy now</span><span class="card__price">$00.00</span>
      </div>
      <div class="card">
        <div class="card__photo card__photo--mix" role="img" aria-label="Photo of assorted skincare products"></div>
        <div class="card__name">IPSUM DOLOR SIT</div>
        <p class="card__text">Consectetur adipiscing elit, sed iusmod tempor incid utaboreolore magna aliqua.</p>
        <span class="card__buy">buy now</span><span class="card__price">$00.00</span>
      </div>
    </aside>

    <div class="abs block" style="top:174px">
      <h2 class="block__title" style="font-weight:400">Sed ut perspiciatis unde omnis natus error sitvolup<span class="go"></span></h2>
      <p class="block__lead">Sed ut perspiciatis unde omnis iste natus</p>
      <p class="block__text">Error itatem accusantium doloremque laudanti ttam aperiam, eue ipsa quae ab illo inventore veritteasi archecto beatatae dicta sunt explicabo. Nemoipsam oluptatem quia voluptas.</p>
    </div>
    <div class="abs block__rule" style="top:232px"></div>
    <div class="abs block" style="top:249px"><h2 class="block__title" style="font-weight:400">Register for our newsletter<span class="go"></span></h2></div>
    <svg class="abs icon" style="left:119px;top:265px" viewBox="0 0 28 34"><rect x="4" y="3" width="16" height="22" rx="1" fill="#3fa33a" transform="rotate(-12 12 14)"/><rect x="6" y="5" width="12" height="18" fill="#e8f2d8" transform="rotate(-12 12 14)"/><line x1="12" y1="28" x2="25" y2="10" stroke="#333" stroke-width="2"/></svg>
    <div class="abs block__body" style="top:264px">
      <p class="block__lead" style="margin:0">Perspiciatis unde omnis iste natus</p>
      <p class="block__text">Error itatem accusantium doloremque laudanti totam aperiam, eue ipsa quae ab illo inventore veritis easi archecto beatatae dicta sunt explicabo. Nemo ipsam oluptatem quia voluptas sit aspernatur.</p>
    </div>
    <div class="abs block__rule" style="top:302px"></div>
    <div class="abs block" style="top:318px"><h2 class="block__title" style="font-weight:400">Contact Us<span class="go"></span></h2></div>
    <svg class="abs icon" style="left:119px;top:333px" viewBox="0 0 28 34"><rect x="3" y="8" width="22" height="18" rx="3" fill="#4a8a4a"/><rect x="7" y="4" width="14" height="6" rx="3" fill="#2e6b35"/><rect x="8" y="12" width="12" height="10" fill="#dfe9d6"/></svg>
    <div class="abs block__body" style="top:334px">
      <p class="block__lead" style="margin:0">Error itatem accusantium</p>
      <p class="block__text">Dolremque laudantium, totam aperiam, e ipsa quae ab illo inventore veritatis easi archecto beatatae dicta sunt explicabo. Nemo ipsam oluptatem quia voluptas sit aspernatur.</p>
    </div>

    <div class="abs news">
      <div class="news__head">News &amp; Events</div>
      <div class="news__item">
        <div class="news__title">Unde omnis iste natus error itatem</div>
        <div class="news__date">Posted: 12/07/2008</div>
        <p class="news__text">Doloremque laudantium, tperiam, eue ipsa quae <u>ab illontore veritatis</u> easi archecto beatatae.</p>
      </div>
      <div class="news__item" style="padding-top:9px">
        <div class="news__title">Doloremque laudantiu tperiam</div>
        <div class="news__date">Posted: 12/07/2008</div>
        <p class="news__text">Daudantium, tperiam, eue ipsquae ab illontore veritatis easi archecto beatatadicta <u>sunt explicabo</u>. Nemo ipsam oluptatem quiae</p>
      </div>
    </div>

    <svg class="abs badge" viewBox="0 0 60 60"><defs><radialGradient id="bgB" cx=".4" cy=".35"><stop offset="0" stop-color="#a8cf45"/><stop offset="1" stop-color="#5e9425"/></radialGradient></defs><circle cx="30" cy="30" r="29" fill="url(#bgB)"/><path d="M44 4 L58 18 L46 16 Z" fill="#e9efe0"/></svg>
    <div class="badge__text">
      <div class="badge__big">-5%</div>
      <div class="badge__small">by online order</div>
      <div class="badge__link">click here</div>
    </div>

    <footer class="abs footer"><div class="footer__links">Company &nbsp;|&nbsp; Products &nbsp;|&nbsp; Download &nbsp;|&nbsp; Support &nbsp;|&nbsp; Contacts</div></footer>
  </section>
  <div class="caption" style="left:424px">HOME PAGE</div>

  <!-- Product page -->
  <section class="page page--product">
    <div class="abs brand"><span class="brand__dot"></span><span class="brand__name">Kestrel Trading</span></div>
    <div class="abs phone">
      <svg width="11" height="11" viewBox="0 0 12 12"><rect width="12" height="12" rx="2" fill="#8dbb2e"/><path d="M3.5 2.5c.6-.3 1.2 0 1.4.6l.4 1.2c.1.4-.1.8-.4 1l-.4.3c.4.9 1.1 1.6 2 2l.3-.4c.3-.3.7-.5 1-.4l1.2.4c.6.2.9.8.6 1.4-.4.8-1.3 1.2-2.2.9C5.3 8.8 3.2 6.7 2.6 4.6c-.3-.9.1-1.8.9-2.1z" fill="#fff"/></svg>
      07 5000 3172
    </div>
    <nav class="abs nav"><span>Home</span><span>About Us</span><span>Products</span><span>Ordering</span><span>Contact Us</span></nav>

    <div class="abs banner">
      <div class="banner__photo" role="img" aria-label="Photo of jojoba oil bottles and red gift boxes"></div>
      <div class="banner__title">Welcome to Our Site!</div>
      <p class="banner__text">Sed ut perspiciatis unde omnis iste natus error sit voluptatem accustium doremque launtium.</p>
      <div class="banner__button">CLICK HERE TO LEARN MORE</div>
    </div>

    <ul class="abs dropdown" style="list-style:none">
      <li class="dropdown__top">Willow's Cottage</li>
      <li class="dropdown__item">Jojoba Oil</li>
      <li class="dropdown__item dropdown__item--on">Southern Meadow Ess.</li>
      <li class="dropdown__item">Product</li><li class="dropdown__item">Product</li><li class="dropdown__item">Product</li>
      <li class="dropdown__item">Product</li><li class="dropdown__item">Product</li><li class="dropdown__item">Product</li>
      <li class="dropdown__item">Product</li><li class="dropdown__item">Product</li><li class="dropdown__item">Product</li>
      <li class="dropdown__item">Product</li><li class="dropdown__item">Product</li><li class="dropdown__item">Product</li>
    </ul>

    <h1 class="abs product__title" style="font-weight:400">Product</h1>
    <div class="abs product__list">
      <p class="product__lead">Aenean nonummy hendrerit mauris</p><p class="product__text">Phasellus porta. Fusce suscipit varius mi.</p>
      <p class="product__lead">Cum sociis natoque penatibus et</p><p class="product__text">Magnis dis parturient montes, nascetur ridiculus mus.</p>
      <p class="product__lead">Fusce feugiat malesuada odio</p><p class="product__text">Morbi nunc odio, gravida at, cursus nec lorem.</p>
      <p class="product__lead">Maecenas tristique orci ac sem</p><p class="product__text">Duis ultricies pharetra magna. Donec accumsan.</p>
      <p class="product__lead">Donec sit amet eros</p><p class="product__text">Lorem ipsum dolor sit amet, consectetuer elit.</p>
      <p class="product__lead">Mauris fermentum dictum magna</p><p class="product__text">Sed laoreet aliquam leo. Ut tellus dolor, dapibus.</p>
    </div>
    <div class="abs enquire">ENQUIRE NOW</div>
    <div class="abs product__photo" role="img" aria-label="Photo of a group of health supplement jars"></div>

    <div class="abs strip__rule"></div>
    <div class="abs strip">
      <svg width="6" height="8" viewBox="0 0 6 8"><path d="M5 0 L0 4 L5 8Z" fill="#555"/></svg>
      <div class="strip__thumb" role="img" aria-label="Product thumbnail"></div>
      <div class="strip__thumb strip__thumb--soap" role="img" aria-label="Soap product thumbnail"></div>
      <div class="strip__thumb strip__thumb--red" role="img" aria-label="Jojoba gift pack thumbnail"></div>
      <div class="strip__thumb" role="img" aria-label="Product thumbnail"></div>
      <div class="strip__thumb" role="img" aria-label="Product thumbnail"></div>
      <div class="strip__thumb" role="img" aria-label="Product thumbnail"></div>
      <div class="strip__thumb" role="img" aria-label="Product thumbnail"></div>
      <div class="strip__thumb" role="img" aria-label="Product thumbnail"></div>
      <svg width="6" height="8" viewBox="0 0 6 8"><path d="M1 0 L6 4 L1 8Z" fill="#555"/></svg>
    </div>

    <footer class="abs footer"><div class="footer__links">Company &nbsp;|&nbsp; Products &nbsp;|&nbsp; Download &nbsp;|&nbsp; Support &nbsp;|&nbsp; Contacts</div></footer>
  </section>
  <div class="caption" style="left:797px">PRODUCT PAGE</div>

</div>
</body>
</html>
```